Interior designer needs a product brochure design for a bedding collection

Hello designers,
My name is Marisol, i need your professional services.
I am after a product brochure design for a bedding collection. (Please see attached bedding word document).
This collection will be sold in a black box with gold (foil) logo on the front.
I have attached a design of my business card for visual reference (matt black paper with black gloss A). As well as Tormund Vessky product marketing brochure which i love, in particular the way its layed out over several pages.
Personally, i feel this brochure will need to be layout out in a similar way otherwise it is too much information on one page.
Please use your creative license in regards to the size, shape, layout, materials used etc etc, but also be mindful of the overall costs. Having said that, i will be guided by you and will want to keep true to your vision also.
Thank you for your time and creativity
MarisolV

Target Market(s)

High end luxury market

Industry/Entity Type

Interior

Font styles to use
Other font styles liked:
• ebrima

Requirements
Must have
• logo
• information attached in word document including washing instructions
Nice to have
• Creative license
• I am told ebrima is the matching font, please let me know otherwise.
Should not have
• Over sized paper, i am fine with A4 and or smaller

```html
<!DOCTYPE html>
<html lang="en">
<head>
<meta charset="utf-8">
<title>MarisolV Bedding Collection – Brochure Spread</title>
<link rel="stylesheet" href="https://fonts.googleapis.com/css2?family=Courier+Prime&display=swap">
<style>
  :root {
    --ink: #060606;
    --ivory: #faf7f4;
    --gold: #b8996a;
    --gold-deep: #8f7448;
    --gold-soft: #d6bf8d;
    --photo-dark: #0b0b0b;
    --photo-mid: #2a2723;
    --photo-gold: #a88438;
  }
  * { margin: 0; padding: 0; box-sizing: border-box; }
  html, body { width: 1200px; height: 848px; overflow: hidden; background: var(--ink); }
  body { font-family: "Courier Prime", "Courier New", monospace; color: var(--gold); }

  .spread { position: relative; width: 1200px; height: 848px; overflow: hidden; }
  .panel { position: absolute; top: 0; height: 848px; }
  .panel--philosophy { left: 0; width: 408px; background: var(--ink); }
  .panel--colours { left: 408px; width: 398px; background: var(--ivory); }
  .panel--collection { left: 806px; width: 394px; background: var(--ink); }

  .copy {
    position: absolute;
    text-align: center;
    text-transform: uppercase;
    font-size: 11px;
    line-height: 20px;
    letter-spacing: 0.6px;
  }
  .copy p + p { margin-top: 20px; }

  /* Philosophy panel */
  .crest { position: absolute; left: 66px; top: 92px; width: 290px; height: 146px; }
  .crest__name {
    position: absolute; left: 0; width: 100%; top: 40px;
    text-align: center; font-size: 11px; letter-spacing: 2px; color: var(--gold);
  }
  .crest__title {
    position: absolute; left: 0; width: 100%; top: 77px;
    text-align: center; font-size: 18px; letter-spacing: 4px; color: var(--gold);
  }
  .philosophy-copy { left: 70px; top: 271px; width: 270px; }

  /* Colour-way panel */
  .colour-frame {
    position: absolute; left: 74px; top: 197px; width: 267px; height: 311px;
    border: 1.5px solid var(--gold-deep);
  }
  .colour-frame__name {
    position: absolute; left: 0; width: 100%; top: 56px;
    text-align: center; font-size: 13px; letter-spacing: 2px; color: var(--gold-deep);
  }
  .colour-frame__list {
    position: absolute; left: 0; width: 100%; top: 130px;
    text-align: center; text-transform: uppercase;
    font-size: 15px; line-height: 31.5px; letter-spacing: 0.5px; color: var(--gold-deep);
    list-style: none;
  }
  .mix-note { left: 72px; top: 563px; width: 270px; color: var(--gold-deep); }

  /* Collection panel */
  .collection-heading {
    position: absolute; left: 0; width: 100%; top: 100px;
    text-align: center; font-size: 18px; letter-spacing: 1.5px; font-weight: normal;
  }
  .flourish {
    position: absolute; left: 92px; top: 146px; width: 210px; height: 54px;
    background: linear-gradient(90deg, transparent, var(--gold-deep) 30%, var(--gold-soft) 50%, var(--gold-deep) 70%, transparent);
    opacity: 0.55;
  }
  .collection-tagline {
    position: absolute; left: 0; width: 100%; top: 216px;
    text-align: center; font-size: 18px; letter-spacing: 2px; font-weight: normal;
  }
  .collection-copy { left: 82px; top: 317px; width: 240px; }
  .bottle-photo {
    position: absolute; left: 27px; top: 562px; width: 367px; height: 286px;
    background:
      radial-gradient(ellipse 60px 140px at 305px 90px, var(--photo-gold), transparent 70%),
      radial-gradient(ellipse 180px 90px at 190px 210px, var(--photo-mid), transparent 75%),
      var(--photo-dark);
  }
</style>
</head>
<body>
<main class="spread">

  <section class="panel panel--philosophy">
    <div class="crest">
      <svg width="290" height="146" viewBox="0 0 290 146" aria-hidden="true">
        <polygon points="2,73 145,2 288,73 145,144" fill="none" stroke="var(--gold)" stroke-width="1.3"/>
      </svg>
      <span class="crest__name">MARISOLV</span>
      <h2 class="crest__title">PHILOSOPHY</h2>
    </div>
    <div class="copy philosophy-copy">
      <p>Ultimate design requires a constant pursuit of perfection. Taking the best that exists and making it better. Or,if it doesn't exist, create it.</p>
      <p>Answering the perennial question of style versus function, MarisolV has fused technology and style to create a bedding collection that is sumptuously smooth, silky and luxurious to the touch.</p>
      <p>She has used the finest available materials combined with a centuries-old manufacturing process to produce this exclusive 900 thread-count collection made from 100% single, fine, long-staple combed cotton, representing 3% of the world's highest-grade cotton production.</p>
    </div>
  </section>

  <section class="panel panel--colours">
    <div class="colour-frame">
      <span class="colour-frame__name">MARISOLV</span>
      <ul class="colour-frame__list">
        <li>Available</li>
        <li>in two colour ways</li>
        <li>Dreamy White</li>
        <li>and</li>
        <li>Penthouse Grey</li>
      </ul>
    </div>
    <div class="copy mix-note">
      <p>All items are sold separately for you to mix and match and personalise to your individual style.</p>
    </div>
  </section>

  <section class="panel panel--collection">
    <h1 class="collection-heading">HOTEL LUXURY COLLECTION</h1>
    <div class="flourish" role="img" aria-label="Gold ornamental flourish divider"></div>
    <h2 class="collection-tagline">5 STAR LUXURY AT HOME</h2>
    <div class="copy collection-copy">
      <p>MarisolV bedding collection in Dreamy White and Penthouse Grey is available in queen and king size duvet cover, fitted sheet, flat sheet, standard pillowcase, tailored pillowcase, king standard pillowcase and Euro tailored pillowcase.</p>
    </div>
    <div class="bottle-photo" role="img" aria-label="Photograph of a gold-foiled champagne bottle chilling in a black ice bucket"></div>
  </section>

</main>
</body>
</html>
```